BoltCrewBoard Postcard Campaign

We need a postcard design for our company, BoltCrewBoard.com - we are a job board for mechanics and auto technicians. We are sending a postcard to 1000 auto shops and trucking companies across the US to try to get them to come to our website and purchase a job pack and post a job posting. We will be offering them a promotion of "Save $20 on your first job post. Enter 'SUMMER20' at checkout."

We would like to see designs that are consistent with our website theme. The final design should communicate:
- Access to a targeted and local audience of only auto and truck mechanics and technicians
- Search 50,000 resumes
- Money back guarantee

Target Market(s)

Auto mechanic shops, car dealerships looking for mechanics, truck fleet management looking for technicians

Industry/Entity Type

It Company

Font styles to use
Sans Serif

Colors
0392cd
ec1f27
1b1b1b
cbcbcb
ffffff
3277b5

Requirements
Must have
• See content/copy upload
• - Match website color scheme and look and feel
Should not have
• No photos that look like stock photos - preferably steer away from photos unless it looks great

```html
<!DOCTYPE html>
<html lang="en">
<head>
<meta charset="utf-8">
<title>BoltCrewBoard Postcard</title>
<link rel="stylesheet" href="https://fonts.googleapis.com/css2?family=Roboto+Condensed:wght@300;400;700&display=swap">
<style>
:root{
  --blue-deep:#1d3f8f;
  --blue-mid:#3277b5;
  --blue-bright:#0392cd;
  --blue-sky:#35b4e8;
  --red:#ec1f27;
  --red-dark:#a5141a;
  --salmon:#f2a08a;
  --ink:#1b1b1b;
  --grey:#cbcbcb;
  --white:#ffffff;
  --gold:#f5a81c;
  --page:#e9e9e9;
}
*{box-sizing:border-box;margin:0;padding:0}
html,body{width:1200px;height:1200px;overflow:hidden}
body{background:var(--page);position:relative;font-family:"Roboto Condensed",Arial,sans-serif;color:var(--ink)}
.card{position:absolute;background:var(--white);box-shadow:0 2px 6px rgba(0,0,0,.25)}
.card-front{left:34px;top:26px;width:730px;height:564px}
.card-back{left:399px;top:615px;width:730px;height:565px}

/* front */
.front-art{position:absolute;left:18px;top:17px;width:694px;height:529px;overflow:hidden;background:var(--ink)}
.front-body{position:absolute;left:0;top:60px;width:694px;height:400px;
  background:radial-gradient(ellipse 420px 300px at 470px 180px,var(--blue-sky) 0%,var(--blue-bright) 20%,var(--blue-mid) 45%,var(--blue-deep) 100%)}
.gear-area{position:absolute;left:420px;top:120px;width:300px;height:340px;border-radius:50%;
  background:radial-gradient(circle at 40% 40%,rgba(53,180,232,.55),rgba(29,63,143,.35) 70%,transparent 72%)}
.front-corner{position:absolute;left:0;top:0}
.headline-ribbon{position:absolute;left:53px;top:27px;width:590px;height:73px;background:#22479a;
  border:1px solid #3a62b4;box-shadow:0 3px 6px rgba(0,0,0,.45);
  color:var(--white);font-weight:300;font-size:39px;line-height:71px;text-align:center;letter-spacing:-.5px;white-space:nowrap}
.benefits{position:absolute;left:52px;top:129px;list-style:none;color:var(--white);font-weight:300;font-size:16.5px;line-height:21.5px;white-space:nowrap}
.benefits li{position:relative;padding-left:43px;margin-bottom:14px}
.benefits li::before{content:"";position:absolute;left:2px;top:50%;width:24px;height:24px;margin-top:-12px;border-radius:50%;background:var(--white)}
.brand-front{position:absolute;left:60px;top:340px;width:273px;text-align:center;color:var(--white);font-weight:700;white-space:nowrap}
.brand-name{font-size:27px;letter-spacing:0;line-height:34px}
.brand-phone{font-size:23px;line-height:34px}
.brand-mark{position:absolute;left:352px;top:326px;width:58px;height:58px;border-radius:50%;background:var(--white)}
.front-footer{position:absolute;left:0;top:462px;width:694px;height:67px;
  background:linear-gradient(#2b2b2b,#0c0c0c);border-top:4px solid #3b3b3b;
  color:var(--blue-sky);font-weight:300;font-size:17px;line-height:22px;text-align:center;padding-top:14px;white-space:nowrap}

/* back */
.back-header{position:absolute;left:18px;top:18px;width:400px;height:128px;
  background:radial-gradient(ellipse 300px 120px at 200px 130px,var(--blue-bright),var(--blue-mid) 55%,var(--blue-deep));color:var(--white);font-weight:700;white-space:nowrap}
.back-header .brand-name{position:absolute;left:26px;top:38px;width:270px;text-align:center}
.back-header .brand-phone{position:absolute;left:26px;top:74px;width:270px;text-align:center}
.back-header .brand-mark{left:316px;top:24px}
.pitch{position:absolute;left:18px;top:160px;width:400px;text-align:center;text-transform:uppercase;line-height:25px}
.pitch .soft{font-weight:300;font-size:17px}
.pitch .bold{font-weight:700;font-size:21px}
.promo-ribbon{position:absolute;left:47px;top:265px;width:343px;height:43px;background:var(--red);
  color:var(--white);font-weight:400;font-size:23px;line-height:43px;text-align:center;box-shadow:0 2px 3px rgba(0,0,0,.25);white-space:nowrap}
.ribbon-fold{position:absolute}
.back-triangle{position:absolute;left:18px;top:335px}
.promise{position:absolute;left:45px;top:340px;width:350px;text-align:center;text-transform:uppercase;font-size:13px;line-height:17.5px;font-weight:400}
.social{position:absolute;left:100px;top:424px;width:240px;text-align:center;font-size:14px;white-space:nowrap}
.social strong{font-size:17px;font-weight:700}
.social-row{display:flex;justify-content:center;gap:8px;margin-top:10px}
.social-row span{width:32px;height:32px;border-radius:4px;background:var(--blue-mid)}
.price-badge{position:absolute;left:318px;top:410px;width:104px;height:104px;border-radius:50%;background:var(--gold);
  color:var(--white);text-align:center;transform:rotate(-10deg)}
.price-badge .amt{display:block;font-weight:300;font-size:50px;line-height:50px;padding-top:16px}
.price-badge .off{display:block;font-weight:300;font-size:18px;line-height:18px}
.stamp-box{position:absolute;left:581px;top:28px;width:122px;height:118px;border:1px solid var(--ink)}
.address-line{position:absolute;left:460px;width:240px;height:1px;background:#555}
</style>
</head>
<body>

<article class="card card-front">
  <div class="front-art">
    <div class="front-body">
      <div class="gear-area" role="img" aria-label="Large blue gear with wrench symbol, fading into the background"></div>
    </div>
    <svg class="front-corner" width="694" height="529" viewBox="0 0 694 529" aria-hidden="true">
      <polygon points="75,60 128,49 128,60" fill="var(--red-dark)"/>
      <polygon points="565,100 640,100 640,115 578,120" fill="var(--red-dark)"/>
      <polygon points="0,350 0,460 80,460" fill="var(--red)"/>
      <polygon points="0,285 0,325 90,460 70,460 0,350" fill="#8a8fc4" opacity=".8"/>
      <polygon points="0,290 96,460 84,460 0,310" fill="#b7bbe2"/>
    </svg>
    <h1 class="headline-ribbon">FIND YOUR NEXT MECHANIC TODAY!</h1>
    <ul class="benefits">
      <li>Post a job with us and get access to hundreds of<br>qualified technicians in your area.</li>
      <li>Includes distribuyion and promotion across<br>multiple&nbsp;&nbsp; job boards, such as HireLane.com,<br>TechRoster, WrenchPost.com etc.</li>
      <li>Search 50,000+ resumes, with&nbsp; new candidates<br>added daily.</li>
    </ul>
    <div class="brand-front">
      <div class="brand-name">BOLTCREWBOARD.COM</div>
      <div class="brand-phone">(800) 555-0142</div>
    </div>
    <span class="brand-mark" aria-hidden="true"></span>
    <footer class="front-footer">CONNECTNG AUTOMOTIVE EMPLOYERS WITH QUALIFIED TECHNICIANS SINCE 2006<br>100% SATISSFACTION GUARANTEED, OR YOUR MONEY BACK</footer>
  </div>
</article>

<article class="card card-back">
  <header class="back-header">
    <div class="brand-name">BOLTCREWBOARD.COM</div>
    <div class="brand-phone">(800) 555-0142</div>
    <span class="brand-mark" aria-hidden="true"></span>
  </header>
  <div class="pitch">
    <div class="soft">Finding good talent</div>
    <div class="bold">Shouldn’t be so hard</div>
    <div class="bold">Get $20 off</div>
    <div class="soft">Your first job post</div>
  </div>
  <svg class="ribbon-fold" style="left:47px;top:253px" width="345" height="68" viewBox="0 0 345 68" aria-hidden="true">
    <polygon points="0,12 44,0 44,12" fill="var(--red-dark)"/>
    <polygon points="300,55 343,55 343,47" fill="var(--red-dark)"/>
  </svg>
  <div class="promo-ribbon">Enter SUMMER20 at checkout</div>
  <svg class="back-triangle" width="110" height="213" viewBox="0 0 110 213" aria-hidden="true">
    <polygon points="0,0 104,213 0,213" fill="var(--salmon)"/>
    <polygon points="0,32 88,213 0,213" fill="var(--red)"/>
  </svg>
  <p class="promise">Connectng automotive employers with qualified technicians since 2006.<br>100% satissfaction guaranteed, or your money back.</p>
  <div class="social">
    Find us @ <strong>boltcrewboard2</strong> on
    <div class="social-row" aria-label="Social profiles"><span></span><span></span><span></span></div>
  </div>
  <div class="price-badge"><span class="amt">$20</span><span class="off">OFF</span></div>
  <div class="stamp-box" aria-label="Stamp area"></div>
  <span class="address-line" style="top:230px"></span>
  <span class="address-line" style="top:293px"></span>
  <span class="address-line" style="top:356px"></span>
  <span class="address-line" style="top:419px"></span>
</article>

</body>
</html>
```